Sudden Tides "Lantern Road" New Single Cover

Create cover artwork for the band Sudden Tides' new single "Lantern Road" being released early 2020. Style, font and graphics to be consistent with band's previous releases and overall brand identity. Visit www.suddentidesband.example and our Spotify page https://music.example.net/artist/7QzWpLx3RtVnKd8e2YbHcJ?si=MUrTgKa4PLe7skvWq2AmZd to view our previous releases and overall brand identity. Some examples attached as well. We are looking for someone to work with on future projects as well.

Lyrics are here: https://docs.example.org/document/d/3KTp9wrn_2ZQa8eXb4Lo_fimH7C5m83Jz4Pd70hrtVcA/edit

Music is here: https://audiostream.example.com/suddentides/lantern-road/s-pzkwa

Font styles to use
Sans Serif

Colors

Designer to choose colors to be used in the design.

Requirements
Must have
• Must be consistent with current brand identity and with prior album / single art.

```html
<!DOCTYPE html>
<html lang="en">
<head>
<meta charset="utf-8">
<title>Sudden Tides – Lantern Road</title>
<link rel="stylesheet" href="https://fonts.googleapis.com/css2?family=Montserrat:wght@400;600&display=swap">
<style>
  :root {
    --teal: #21a5aa;
    --navy: #1f2d5a;
    --amber: #fdb01e;
  }
  html, body {
    margin: 0;
    padding: 0;
    width: 1200px;
    height: 1200px;
    overflow: hidden;
    background: var(--teal);
  }
  .cover {
    display: block;
    width: 1200px;
    height: 1200px;
  }
  .cover__bg { fill: var(--teal); }
  .bar { fill: var(--navy); }
  .title {
    font-family: "Montserrat", sans-serif;
    font-weight: 600;
    font-size: 92px;
  }
  .title--main { fill: var(--amber); }
  .title--reflection { fill: var(--navy); }
  .band-name {
    font-family: "Montserrat", sans-serif;
    font-weight: 400;
    font-size: 52px;
    letter-spacing: 8px;
    fill: var(--navy);
  }
</style>
</head>
<body>
<svg class="cover" viewBox="0 0 1200 1200" xmlns="http://www.w3.org/2000/svg">
  <rect class="cover__bg" width="1200" height="1200"/>

  <g class="top-bars">
    <rect class="bar" x="533" y="0" width="33" height="358"/>
    <rect class="bar" x="631" y="0" width="33" height="180"/>
  </g>

  <g class="title-block">
    <g transform="translate(0 600) scale(1 -0.95) translate(0 -600)">
      <text class="title title--reflection" x="246" y="600" textLength="714" lengthAdjust="spacingAndGlyphs">LANTERN ROAD</text>
    </g>
    <text class="title title--main" x="246" y="600" textLength="714" lengthAdjust="spacingAndGlyphs">LANTERN ROAD</text>
  </g>

  <g class="drip-bars">
    <rect class="bar" x="248" y="598" width="17" height="254"/>
    <rect class="bar" x="300" y="598" width="16" height="162"/>
  </g>

  <g class="band-name-block">
    <text class="band-name" x="600" y="1000" text-anchor="middle">SUDDEN</text>
    <text class="band-name" x="600" y="1078" text-anchor="middle">TIDES</text>
  </g>
</svg>
</body>
</html>
```